Guarenteed! - Homepage Website Design - Coding not required- Winner to complete further pages

Hi all,

We're looking at redesigning our current website with a few adjustments to other pages but the main adjustments will be on the homepage which is what this design request is for. Please note : any of these ideas can be changed if you have something particularly different / special in mind etc.

P.S Coding is not required, just a design.

- Our website -

Our website is simply a price comparison website that allows customers to find companies within their area at the best price. The products available are mostly related to the vehicle trade and all refer to vinyl. This includes the likes of vehicle window tint, vehicle colour change vehicle wrap, vehicle signage as well as other cosmetic vinyl modifications. We allow the customer to search for their product within their chosen area and receive a list of companies who supply their product within that area. From here they can compare prices and view further details on the company.

- What we're looking to do -

We're looking first of all to adjust how the website homepage is displayed, this includes adding images and adjusting the colours that are explained below:

First of all, we look to spread out each of the 12 products (which can be seen on the website as it stands) and add an image to each of the products (all being spaced out as shown in our sketch)

We've been told the website looks too busy so we're thinking if we adjust the colours to more simplier neutral colours as well as the main focus of the website being on the 12 images, that would be great.

- Logo + Banner -

Logo to remain top left although banner may be removed / adjusted to make simplier.

- Colours -

Adjustments - Colours shades
We want the website to still look exciting but simplify the colours. Needs to be kept up to date with the colours / textures etc (bright colours to highlight keypoints)
We're still looking to use either blue or orange or maybe both to highlight these keypoints but the main website to be light colours and maybe even black on white background. The entire homepage can be adjusted colour wise if you feel it fits into your theme including menu bars, banners etc. The key is to get this right with being not too overpowering with the colours but still look interesting and up to date.

- 1 - 4 steps banner - (text may change)

This sits just under the logo and explains to the user how easy the website is to use and the steps they need to take. This may change to a 1 - 5 steps but we're looking to have this designed once the overall colours / theme of the website is sorted.

- 12 images - 4 x 3

This is the main focus of the website and will be the main focus of what the customer sees first of all. This will be where they select their product and then underneath, enter their postcode and distance they would like to search within. As explained further up, we have some of the product images available so if you can where possible add these to the design and then duplicate the images on those we currently don't have available.

- 12 Images -Titles -

These titles will be in this order from left to right and etc

- Colour Change Wrap
- Printed Vehicle Wrap
- Window Tint
- Headlight Tint
- Vehicle Signage
- Shop Signage
- Roof Vinyl Wrap
- Bonnet Vinyl Wrap
- Carbon Fibre Vinyl
- Stickerbomb Vinyl
- Clear Protective Vinyl
- Wheel Refurb

Text to be quite large, centered and with the o to the left of the title. Short titles like 'Window Tint' should fit on one line in the middle of the box where as titles such as ' Stickerbomb Vinyl Wrap' should have the 'Stickerbomb Vinyl' on the first line with the 'Wrap' on the line below. The background of this text is up to experient, might be worth just a simple colour or it might be worth using a bright blue or orange to keep in with the theme of the logo etc.

These will also have the circle tick box to the left of the title (as on the current website) where the customer clicks to select the product they have available.
We were also thinking that if when the customer ticks the circle on their selected box, the box is highlighted in some way to show this.

- Search Block -

This will appear under the 12 images and allows the customer to input their postcode and distance for the search criteria. Colours on this can of course be adjusted to keep in theme with the website.

- Under the 12 Images -

- Block underneath the 12 images and search block -

To the left will be some key bullet points about the website - maybe 4 or 5 with a green tick to the left of this. Background colour will probably be best to be a light colour, possibly grey.

Then to the right of this will appear 4 images, 2 before and 2 after when applying these products. Images to be used aren't fully decided on and we would like this stage of the design left to the end when the rest of the theme etc have been decided on.

Attached images are as follows :
- How the website looks as it stands
- The fold line on the website (obviously important)
- Our rough sketch of how we'd like the website homepage to look.
- We have 7 of the images ready that are all attached in this one file. Please duplicate the images on those that currently don't have the image available.

We will also be requesting a website developer to put this into action if our current designer falls through so please feel free to contact us if potentially interested.

The layout can change if you can think of something particular different / unique that works with this design. The main idea is to not only get the 12 products on view to the viewers but also the keypoints and before and after images.

Any questions, please ask away as we're bound to have forgotten a few things.

Thanks and good luck!

Hi all, keep the designs coming.

We haven't quite seen that extra special design we're after. As stated, we're after something fairly simple to suit the youth as well as the middle aged but we're also after something that bit special.

Colours to concentrate on are still and orange etc although feel free to use other colours if you have anything special in mind.

Please experience and we'll give you our honest feedback.

Many thanks all and good luck!

Hi all, this is a message to all the designers.

Some good designs coming in but we're still after that something special for the website design. Keep the designs coming and please feel free to experiment with the design colours, layout etc.

The basic principle of the website needs to remain regarding the 12 products, search within block and 4 steps all appearing on the homepage.

The 4 steps seems to work best when it's got text as well as some simple images next to this.

A variation with the product titles with how to display this, some designers have gone with a simple white background whereas others have gone with colours. Please experiment here and where possible, add a contract / texture to the colour. Please remember the product titles needs to be clear, centured and with the circle tick box to the left of it. 

We're after a fairly simple design although we need it to look 21st century, up to date as well as interesting. The key points straight away are the 4 steps as well as the 12 products so try to guide the viewer to these areas a little.

White background behind the 12 images seems to be a much, although a light colour could possibly work.

The keypoints underneath these 12 products are too very important as it outlines what we do etc. Tick colour can vary.

Next to these keypoints will be the 'before' and 'after' images, these images needs to be fairly small and ensure there is white background around the image itself.

Good luck all and any questions, feel free to ask away.

Thanks!

Hi,

 Thank you for your time and effort with these designs, we are very nearly there with the design but we've thought of something that may work for the homepage. A curved arrow from step 1 pointing to the products, this may or may not work but feel free to give it a go.

Many thanks,

Thank you to everyone for your time and efforts with the design. It's hugely appreciated so thank you all once again.

Wish you all the luck in the future.

Trade

Serif
Sans Serif

```html
<!DOCTYPE html>
<html lang="en">
<head>
<meta charset="utf-8">
<title>Wrapmatch – Compare Vinyl Installers</title>
<link href="https://fonts.googleapis.com/css2?family=Arimo:ital,wght@0,400;0,700;1,400;1,700&display=swap" rel="stylesheet">
<style>
:root{
  --page:#e6e6e6;
  --white:#ffffff;
  --ink:#111111;
  --orange:#f7941d;
  --orange-light:#fbaa3c;
  --blue:#3e5795;
  --blue-light:#6d86bd;
  --side:#d2d2d2;
  --rule:#dddddd;
  --btn:#808080;
  --van-tone-a:#b9c7d3;
  --van-tone-b:#a3b39e;
  --car-tone-a:#9a9a9a;
  --car-tone-b:#b8544c;
}
*{box-sizing:border-box;margin:0;padding:0}
html,body{width:1152px;height:1200px;overflow:hidden}
body{background:var(--page);font-family:"Arimo",Arial,sans-serif;color:var(--ink);position:relative}
.sheet{position:absolute;left:52px;top:0;width:1040px;height:1200px;background:var(--white);box-shadow:0 0 12px rgba(0,0,0,.25)}
.abs{position:absolute}

/* header */
.brand{left:30px;top:52px;display:flex;align-items:center;gap:12px}
.brand-dot{width:34px;height:34px;border-radius:50%;background:var(--orange)}
.brand-name{font-size:40px;font-weight:700;color:#4a4a4a;letter-spacing:1px}
.nav{right:48px;top:104px;display:flex;font-size:13px;color:#222}
.nav a{color:inherit;text-decoration:none;padding:0 15px;border-left:1px solid #222;line-height:12px}
.nav a:first-child{border-left:none;color:var(--orange)}

/* steps band */
.steps{left:0;top:138px;width:1040px;height:160px;background:radial-gradient(ellipse at 50% 60%,var(--blue-light),var(--blue) 75%);color:var(--white)}
.steps-title{left:20px;top:28px;font-size:22px;font-style:italic}
.step{top:76px;display:flex;align-items:center;gap:6px;font-size:20px;font-weight:700;font-style:italic;line-height:25px}
.steps-rule{left:0;top:298px;width:1040px;height:5px;background:var(--ink)}

/* products */
.divider{width:2px;top:343px;height:577px;background:var(--rule)}
.tile{width:232px;height:92px}
.tile-photo{left:0;top:0;width:130px;height:92px;border-top:3px solid var(--ink);border-bottom:3px solid var(--ink);background:linear-gradient(135deg,var(--van-tone-a),var(--van-tone-b))}
.tile-label{left:130px;top:7px;width:102px;height:70px;background:linear-gradient(135deg,var(--orange-light),var(--orange));color:var(--white);padding:6px 0 0 24px;font-size:16px;line-height:18px}
.tile-label::before{content:"";position:absolute;left:-12px;top:22px;border:12px solid transparent;border-right-color:var(--orange-light);border-left:0}
.tile-label .big{font-size:23px;line-height:24px}
.radio{position:absolute;left:7px;top:9px;width:11px;height:11px;border-radius:50%;background:var(--white);border:3px solid #555}

/* sidebar */
.side{left:787px;top:303px;width:253px;height:634px;background:var(--side)}
.side h2{position:absolute;left:26px;top:46px;font-size:29px;font-weight:400;font-style:italic;line-height:36px}
.side-rule{left:10px;top:123px;width:233px;height:1px;background:#eee}
.side-intro{left:26px;top:134px;width:215px;font-size:14px;font-style:italic;line-height:19px;white-space:nowrap}
.point{left:30px;width:210px;font-size:18px;font-style:italic;line-height:21px;padding-left:24px}
.point::before{content:"";position:absolute;left:0;top:4px;border:8px solid transparent;border-left:13px solid var(--orange);border-right:0}

/* search */
.search{left:0;top:937px;width:1040px;height:40px;background:linear-gradient(100deg,var(--blue) 0%,var(--blue) 60%,#6479b1 61%,#7b8fc3 100%);color:var(--white);font-size:17px}
.search-label{left:197px;top:11px}
.field{top:10px;height:21px;background:var(--white);font-size:10px;color:#bbb;padding:5px 6px}
.search-of{left:503px;top:10px}
.search-btn{left:698px;top:10px;width:84px;height:22px;background:var(--btn);border:1px solid #ccc;text-align:center;font-size:15px;line-height:20px}

/* remodels */
.remodels-title{left:18px;top:990px;font-size:23px;font-style:italic;font-weight:400}
.cap{font-size:11px;color:var(--ink)}
.photo{background:linear-gradient(135deg,var(--car-tone-a),var(--car-tone-b))}
.cta-title{left:645px;top:999px;font-size:24px;font-style:italic}
.cta-sub{left:645px;top:1030px;font-size:19px;font-style:italic;color:var(--blue)}
.cap-lg{font-size:16px}
.foot-rule{left:0;top:1192px;width:1040px;height:8px;background:var(--ink)}
</style>
</head>
<body>
<div class="sheet">

  <header>
    <div class="abs brand"><span class="brand-dot"></span><span class="brand-name">WRAPMATCH</span></div>
    <nav class="abs nav"><a>HOME</a><a>ABOUT US</a><a>CONTACT US</a><a>BLOG</a><a>LIST YOUR COMPANY</a></nav>
  </header>

  <section class="abs steps">
    <p class="abs steps-title">Compare Professional Installers Today With These Four Easy Steps...</p>
    <div class="abs step" style="left:22px">
      <svg width="50" height="52" viewBox="0 0 50 52"><path d="M6 48 L34 18 L26 12 L48 4 L42 26 L37 20 L10 51 Z" fill="var(--orange)"/></svg>
      <span>Select Chosen<br>Product</span>
    </div>
    <div class="abs step" style="left:252px">
      <svg width="48" height="60" viewBox="0 0 48 60"><circle cx="28" cy="20" r="16" fill="var(--orange)"/><circle cx="28" cy="20" r="11" fill="#f9a94b"/><path d="M16 32 L4 56" stroke="var(--orange)" stroke-width="6" stroke-linecap="round"/></svg>
      <span>Input Postcode<br>Distance &amp; Search</span>
    </div>
    <div class="abs step" style="left:526px">
      <svg width="46" height="46" viewBox="0 0 46 46"><rect x="2" y="26" width="11" height="20" fill="var(--orange)"/><rect x="17" y="14" width="11" height="32" fill="var(--orange)"/><rect x="32" y="2" width="11" height="44" fill="var(--orange)"/></svg>
      <span>Compare Companies<br>&amp; Prices</span>
    </div>
    <div class="abs step" style="left:810px">
      <svg width="50" height="50" viewBox="0 0 50 50" fill="none"><circle cx="25" cy="25" r="22" fill="var(--orange)"/><ellipse cx="25" cy="25" rx="9" ry="22" stroke="#fbd199" stroke-width="2.5"/><path d="M3 25 H47 M7 13 H43 M7 37 H43 M25 3 V47" stroke="#fbd199" stroke-width="2.5"/></svg>
      <span>Contact Chosen<br>Company</span>
    </div>
  </section>
  <div class="abs steps-rule"></div>

  <main>
    <div class="abs divider" style="left:258px"></div>
    <div class="abs divider" style="left:522px"></div>

    <div class="abs tile" style="left:12px;top:355px"><div class="abs tile-photo" role="img" aria-label="Van with colour change wrap"></div><div class="abs tile-label"><span class="radio"></span>COLOR<br>CHANGE<br><span class="big">WRAP</span></div></div>
    <div class="abs tile" style="left:276px;top:355px"><div class="abs tile-photo" role="img" aria-label="Van with colour change wrap"></div><div class="abs tile-label"><span class="radio"></span>COLOR<br>CHANGE<br><span class="big">WRAP</span></div></div>
    <div class="abs tile" style="left:533px;top:355px"><div class="abs tile-photo" role="img" aria-label="Van with colour change wrap"></div><div class="abs tile-label"><span class="radio"></span>COLOR<br>CHANGE<br><span class="big">WRAP</span></div></div>

    <div class="abs tile" style="left:12px;top:506px"><div class="abs tile-photo" role="img" aria-label="Van with colour change wrap"></div><div class="abs tile-label"><span class="radio"></span>COLOR<br>CHANGE<br><span class="big">WRAP</span></div></div>
    <div class="abs tile" style="left:276px;top:506px"><div class="abs tile-photo" role="img" aria-label="Van with colour change wrap"></div><div class="abs tile-label"><span class="radio"></span>COLOR<br>CHANGE<br><span class="big">WRAP</span></div></div>
    <div class="abs tile" style="left:533px;top:506px"><div class="abs tile-photo" role="img" aria-label="Van with colour change wrap"></div><div class="abs tile-label"><span class="radio"></span>COLOR<br>CHANGE<br><span class="big">WRAP</span></div></div>

    <div class="abs tile" style="left:12px;top:654px"><div class="abs tile-photo" role="img" aria-label="Van with colour change wrap"></div><div class="abs tile-label"><span class="radio"></span>COLOR<br>CHANGE<br><span class="big">WRAP</span></div></div>
    <div class="abs tile" style="left:276px;top:654px"><div class="abs tile-photo" role="img" aria-label="Van with colour change wrap"></div><div class="abs tile-label"><span class="radio"></span>COLOR<br>CHANGE<br><span class="big">WRAP</span></div></div>
    <div class="abs tile" style="left:533px;top:654px"><div class="abs tile-photo" role="img" aria-label="Van with colour change wrap"></div><div class="abs tile-label"><span class="radio"></span>COLOR<br>CHANGE<br><span class="big">WRAP</span></div></div>

    <div class="abs tile" style="left:12px;top:803px"><div class="abs tile-photo" role="img" aria-label="Van with colour change wrap"></div><div class="abs tile-label"><span class="radio"></span>COLOR<br>CHANGE<br><span class="big">WRAP</span></div></div>
    <div class="abs tile" style="left:276px;top:803px"><div class="abs tile-photo" role="img" aria-label="Van with colour change wrap"></div><div class="abs tile-label"><span class="radio"></span>COLOR<br>CHANGE<br><span class="big">WRAP</span></div></div>
    <div class="abs tile" style="left:533px;top:803px"><div class="abs tile-photo" role="img" aria-label="Van with colour change wrap"></div><div class="abs tile-label"><span class="radio"></span>COLOR<br>CHANGE<br><span class="big">WRAP</span></div></div>
  </main>

  <aside class="abs side">
    <h2>How Can We<br>Help You?</h2>
    <div class="abs side-rule"></div>
    <p class="abs side-intro">Intro Text Block Here Place<br>Intro Text Block Here Intro<br>Text Block Here Text Block<br>Here Text Block Here</p>
    <p class="abs point" style="top:235px">Text will input here place holder</p>
    <p class="abs point" style="top:298px">Text will input here place holder</p>
    <p class="abs point" style="top:365px">Text will input here place holder</p>
    <p class="abs point" style="top:433px">Text will input here place holder</p>
  </aside>

  <section class="abs search">
    <span class="abs search-label">SEARCH WITHIN</span>
    <div class="abs field" style="left:349px;width:138px">Enter Miles</div>
    <span class="abs search-of">OF</span>
    <div class="abs field" style="left:542px;width:141px"></div>
    <div class="abs search-btn">SEARCH</div>
  </section>

  <section>
    <h3 class="abs remodels-title">Recent Remodels...</h3>

    <span class="abs cap" style="left:78px;top:1025px">BEFORE</span><span class="abs cap" style="left:192px;top:1025px">AFTER</span>
    <div class="abs photo" style="left:78px;top:1036px;width:105px;height:62px" role="img" aria-label="Red sports car before wrap"></div>
    <div class="abs photo" style="left:192px;top:1036px;width:105px;height:62px" role="img" aria-label="Red sports car after wrap"></div>
    <span class="abs cap" style="left:362px;top:1025px">BEFORE</span><span class="abs cap" style="left:477px;top:1025px">AFTER</span>
    <div class="abs photo" style="left:362px;top:1036px;width:105px;height:62px" role="img" aria-label="Red sports car before wrap"></div>
    <div class="abs photo" style="left:477px;top:1036px;width:105px;height:62px" role="img" aria-label="Red sports car after wrap"></div>

    <span class="abs cap" style="left:78px;top:1115px">BEFORE</span><span class="abs cap" style="left:192px;top:1115px">AFTER</span>
    <div class="abs photo" style="left:78px;top:1126px;width:105px;height:62px" role="img" aria-label="Red sports car before wrap"></div>
    <div class="abs photo" style="left:192px;top:1126px;width:105px;height:62px" role="img" aria-label="Red sports car after wrap"></div>
    <span class="abs cap" style="left:362px;top:1115px">BEFORE</span><span class="abs cap" style="left:477px;top:1115px">AFTER</span>
    <div class="abs photo" style="left:362px;top:1126px;width:105px;height:62px" role="img" aria-label="Red sports car before wrap"></div>
    <div class="abs photo" style="left:477px;top:1126px;width:105px;height:62px" role="img" aria-label="Red sports car after wrap"></div>

    <p class="abs cta-title">Find a Professional Installer Today!</p>
    <p class="abs cta-sub">Search &amp; Save Within Seconds</p>
    <span class="abs cap cap-lg" style="left:648px;top:1066px">BEFORE</span>
    <span class="abs cap cap-lg" style="left:814px;top:1066px">AFTER</span>
    <div class="abs photo" style="left:648px;top:1085px;width:152px;height:90px" role="img" aria-label="Red sports car before wrap"></div>
    <div class="abs photo" style="left:814px;top:1085px;width:152px;height:90px" role="img" aria-label="Red sports car after wrap"></div>
  </section>

  <div class="abs foot-rule"></div>
</div>
</body>
</html>
```